Massage-Creme label for a young pharmacy

We are a young pharmacy which is part of a big union. We developed for a customer a very good massage creme with aloe vera, coconut oil, and many more advantages and as well a massage jelly. All we need is a good and affordable label which is beatiful and helps us to promote our product. As we want to develop further products, it would be very cool to have a corporate label for all upcoming products.

Target Market(s)

professional masseurs and physiotherapists

Industry/Entity Type

Health And Wellness

Font styles to use
Sans Serif
Decorative

Colors

Designer to choose colors to be used in the design.

Requirements
Must have
• Professionally looking design (but I'm sure you are doing so... :-)
Nice to have
• Label can have any shape. What you see is just a bad label with corresponding sizes, so you can imagine how it would look like in the final state.
Should not have
• If possible, the label should not be completely black (although it might look cool) as we are printing it on our own Varnick tq318-dm and black is difficult to print (and very costy).

```html
<!DOCTYPE html>
<html lang="de">
<head>
<meta charset="utf-8">
<title>Massage Crème – Coconut | Aloe Vera</title>
<link rel="stylesheet" href="https://fonts.googleapis.com/css2?family=Oswald:wght@200;400;700&display=swap">
<style>
  :root {
    --page-bg: #f2f2f2;
    --green-light: #8fcf4e;
    --green: #6bb533;
    --green-deep: #3f8f1c;
    --green-text: #5aa629;
    --white: #ffffff;
    --label-white: #f7f8f5;
    --illustration-brown: #8a5a33;
    --illustration-brown-light: #a4764c;
    --illustration-green: #9ccc65;
  }
  * { box-sizing: border-box; margin: 0; padding: 0; }
  html, body {
    width: 1200px;
    height: 1120px;
    overflow: hidden;
    background: var(--page-bg);
    font-family: "Oswald", "Arial Narrow", sans-serif;
  }
  .label {
    position: absolute;
    left: 260px;
    top: 40px;
    width: 680px;
    height: 1040px;
    background: var(--label-white);
    overflow: hidden;
    box-shadow: 0 6px 24px rgba(0,0,0,0.12);
  }
  .label-bands {
    position: absolute;
    inset: 0;
    width: 680px;
    height: 1040px;
  }
  .product-title {
    position: absolute;
    left: 0;
    right: 0;
    top: 120px;
    text-align: center;
    color: var(--white);
    text-shadow: 0 3px 6px rgba(0,0,0,0.18);
  }
  .product-title__main {
    display: block;
    font-weight: 700;
    font-size: 136px;
    line-height: 1;
    letter-spacing: -1px;
  }
  .product-title__sub {
    display: block;
    margin-top: 36px;
    font-weight: 200;
    font-size: 140px;
    line-height: 1;
    letter-spacing: 2px;
  }
  .ingredients {
    position: absolute;
    left: 0;
    right: 0;
    top: 552px;
    text-align: center;
    color: var(--green-text);
    font-weight: 700;
    font-size: 48px;
    line-height: 1.2;
    letter-spacing: 0.5px;
  }
  .badge {
    position: absolute;
    left: 36px;
    top: 660px;
    width: 140px;
    height: 76px;
    border-radius: 50%;
    background: var(--green);
    color: var(--white);
    font-weight: 400;
    font-size: 17px;
    line-height: 1.05;
    text-align: center;
    display: flex;
    align-items: center;
    justify-content: center;
    transform: rotate(-12deg);
    border: 3px solid var(--white);
    box-shadow: 0 2px 5px rgba(0,0,0,0.15);
    z-index: 2;
  }
  .ingredient-illustration {
    position: absolute;
    left: 200px;
    top: 660px;
    width: 420px;
    height: 230px;
    border-radius: 50%;
    background: radial-gradient(ellipse 70% 70% at 40% 55%, var(--illustration-brown) 0%, var(--illustration-brown-light) 45%, var(--illustration-green) 75%, rgba(156,204,101,0) 100%);
  }
  .volume {
    position: absolute;
    left: 0;
    right: 0;
    bottom: 26px;
    text-align: center;
    color: var(--white);
    font-weight: 400;
    font-size: 22px;
  }
</style>
</head>
<body>
  <div class="label">
    <svg class="label-bands" viewBox="0 0 680 1040" aria-hidden="true">
      <defs>
        <linearGradient id="top-band" x1="0" y1="0" x2="0" y2="1">
          <stop offset="0" stop-color="#8fcf4e"/>
          <stop offset="1" stop-color="#5faa2c"/>
        </linearGradient>
        <linearGradient id="bottom-band" x1="0" y1="0" x2="0" y2="1">
          <stop offset="0" stop-color="#7fc343"/>
          <stop offset="1" stop-color="#3f8f1c"/>
        </linearGradient>
      </defs>
      <path d="M0 0 H680 V430 C520 470 300 520 0 540 Z" fill="url(#top-band)"/>
      <path d="M0 470 C220 440 460 400 680 330 V380 C470 450 240 500 0 520 Z" fill="#a6db6b" opacity="0.6"/>
      <path d="M0 500 C240 470 470 420 680 370 V430 C500 470 300 510 0 540 Z" fill="#ffffff" opacity="0.85"/>
      <path d="M0 880 C200 820 460 790 680 830 V1040 H0 Z" fill="url(#bottom-band)"/>
      <path d="M0 860 C220 800 470 770 680 800 V830 C460 790 200 820 0 880 Z" fill="#a6db6b" opacity="0.7"/>
    </svg>

    <h1 class="product-title">
      <span class="product-title__main">MASSAGE</span>
      <span class="product-title__sub">CRÈME</span>
    </h1>

    <p class="ingredients">COCONUT | ALOE VERA</p>

    <div class="ingredient-illustration" role="img" aria-label="Illustration of halved coconuts with aloe vera leaves and slices"></div>

    <div class="badge">energetisch<br>leitend!</div>

    <p class="volume">℮ 1000 ml</p>
  </div>
</body>
</html>
```